Letterhead for New Orthopaedic Surgery Practice

My husband and I are starting our own practice named RB Spine & Vitality Center. We would like to create a nice simple but high class letterhead that doesn't use too much solid color ink when printing. I like the colors dark blue, gold, yellow. Open to other suggestions. We will need to list him and I both on the top of the letterhead. Here is the important information:
Lucinda Pryce, M.D. - Hand and Upper Extremity Surgery
Esi Dankwa, M.D. - Hip & Knee Replacement/General Orthopaedic Surgery
Location: 18735 North Bellhaven Rd
Palm Glen, FL 33418
Phone: 954-218-4635
Fax: 954-581-2264
Email: info@myrbspine.example

The only thing is that the phone and fax numbers will change once we get into our space. I just want to get the design started. I am including several documents which are my previous practice letterhead, my current procedure room letterhead, and our new Logo. The other letterheads are just for examples but please think outside of the box! We would love to see some great designs.

Colors
0054AA
0677BA
7BADD7
CADEEF
E8F1F8
0094D4
00A9DD
6FCCEA
C7EBF8
E9F6FB

Requirements
Must have
• class, elegance, luxury

```html
<!DOCTYPE html>
<html lang="en">
<head>
<meta charset="utf-8">
<title>RB Spine &amp; Vitality Center – Letterhead</title>
<link href="https://fonts.googleapis.com/css2?family=Raleway:wght@400;500;700&family=Lato:wght@400;700&display=swap" rel="stylesheet">
<style>
  :root {
    --navy: #1b2a4e;
    --gold: #c9a25a;
    --paper: #f6f6f6;
    --backdrop: #cdcdcd;
    --body-ink: #5c5f66;
    --rule: #a9abb0;
  }
  * { box-sizing: border-box; margin: 0; padding: 0; }
  html, body { width: 1200px; height: 840px; overflow: hidden; background: var(--backdrop); }
  .sheet {
    position: absolute; top: 96px; width: 496px; height: 648px;
    background: var(--paper); overflow: hidden;
    box-shadow: 0 6px 14px rgba(0,0,0,.22);
  }
  .sheet--blank { left: 86px; }
  .sheet--letter { left: 619px; }
  .masthead { position: absolute; left: 0; top: 0; width: 496px; height: 110px; }
  .practice-mark {
    position: absolute; left: 44px; top: 12px; width: 88px; height: 88px;
    border-radius: 50%; background: var(--paper);
    display: flex; align-items: center; justify-content: center; text-align: center;
    font-family: "Raleway", sans-serif; font-weight: 700; font-size: 10px; line-height: 1.25;
    color: var(--navy); padding: 8px;
  }
  .physicians {
    position: absolute; right: 30px; top: 19px; text-align: right;
    font-family: "Raleway", sans-serif; color: #fff;
  }
  .physician-name { font-weight: 700; font-size: 9.6px; color: var(--gold); line-height: 13px; }
  .physician-specialty { font-weight: 400; font-size: 8px; line-height: 12px; margin-bottom: 1px; }
  .contact-bar {
    position: absolute; left: 44px; width: 408px; top: 612px;
    border-top: 1.2px solid var(--rule); padding-top: 6px;
    display: flex; justify-content: space-between; align-items: center; gap: 5px;
    font-family: "Raleway", sans-serif; font-size: 7px; color: var(--navy); white-space: nowrap;
  }
  .contact-item { display: flex; align-items: center; gap: 2px; }
  .contact-item svg { width: 7px; height: 7px; fill: var(--navy); flex: none; }
  .letter { position: absolute; left: 46px; top: 0; width: 404px; font-family: "Lato", sans-serif; }
  .recipient-name { position: absolute; top: 135px; font-weight: 700; font-size: 10px; color: var(--navy); white-space: nowrap; }
  .recipient-role { position: absolute; top: 150px; font-weight: 700; font-size: 7.2px; color: #111; white-space: nowrap; }
  .letter-date { position: absolute; top: 149px; right: 0; font-size: 7.4px; color: var(--body-ink); white-space: nowrap; }
  .letter-body { position: absolute; top: 183px; width: 404px; font-size: 7.25px; line-height: 11.8px; color: var(--body-ink); text-align: justify; }
  .letter-body p { margin-bottom: 11.8px; }
  .signature { position: absolute; top: 456px; left: 0; width: 106px; height: 26px; background: linear-gradient(90deg, rgba(27,42,78,.18), rgba(27,42,78,.06)); border-radius: 3px; }
  .signer-name { position: absolute; top: 497px; font-weight: 700; font-size: 10px; color: var(--navy); white-space: nowrap; }
  .signer-role { position: absolute; top: 511px; font-weight: 700; font-size: 7.2px; color: var(--body-ink); white-space: nowrap; }
</style>
</head>
<body>

<svg width="0" height="0" style="position:absolute">
  <defs>
    <g id="masthead-art">
      <path fill="#1b2a4e" d="M0,0 H949 V140 C820,178 700,162 560,122 C430,84 320,58 240,55 L160,55 C95,55 45,68 0,86 Z"/>
      <path fill="#c9a25a" d="M0,104 C40,86 90,72 140,66 L148,82 C92,90 42,110 0,132 Z"/>
      <path fill="none" stroke="#c9a25a" stroke-width="9" d="M240,70 C400,76 560,132 700,156 C820,176 900,168 949,158"/>
      <path fill="none" stroke="#1b2a4e" stroke-width="14" d="M245,89 C420,98 580,162 720,192 C840,214 910,206 949,192"/>
    </g>
    <symbol id="icon-phone" viewBox="0 0 24 24"><path d="M6.6 10.8a15.1 15.1 0 0 0 6.6 6.6l2.2-2.2c.3-.3.7-.4 1-.2 1.1.4 2.3.6 3.6.6.6 0 1 .4 1 1V20c0 .6-.4 1-1 1A17 17 0 0 1 3 4c0-.6.4-1 1-1h3.5c.6 0 1 .4 1 1 0 1.3.2 2.5.6 3.6.1.3 0 .7-.2 1z"/></symbol>
    <symbol id="icon-fax" viewBox="0 0 24 24"><path d="M6 2h12v5H6zM4 8h16a2 2 0 0 1 2 2v7h-4v5H6v-5H2v-7a2 2 0 0 1 2-2zm4 8v4h8v-4z"/></symbol>
    <symbol id="icon-mail" viewBox="0 0 24 24"><path d="M2 5h20v14H2zm2 2v.5l8 5 8-5V7zm0 2.8V17h16V9.8l-8 5z"/></symbol>
    <symbol id="icon-pin" viewBox="0 0 24 24"><path d="M12 2a7 7 0 0 1 7 7c0 5-7 13-7 13S5 14 5 9a7 7 0 0 1 7-7zm0 4a3 3 0 1 0 0 6 3 3 0 0 0 0-6z"/></symbol>
  </defs>
</svg>

<section class="sheet sheet--blank">
  <svg class="masthead" viewBox="0 0 949 210" preserveAspectRatio="none"><use href="#masthead-art"/></svg>
  <div class="practice-mark">RB Spine &amp; Vitality Center</div>
  <div class="physicians">
    <div class="physician-name">Esi Dankwa, M.D.</div>
    <div class="physician-specialty">Hip &amp; Knee Replacement / General Orthopaedic Surgery</div>
    <div class="physician-name">Lucinda Pryce, M.D.</div>
    <div class="physician-specialty">Hand and Upper Extremity Surgery</div>
  </div>
  <footer class="contact-bar">
    <span class="contact-item"><svg><use href="#icon-phone"/></svg>954-218-4635</span>
    <span class="contact-item"><svg><use href="#icon-fax"/></svg>954-581-2264</span>
    <span class="contact-item"><svg><use href="#icon-mail"/></svg>info@myrbspine.example</span>
    <span class="contact-item"><svg><use href="#icon-pin"/></svg>18735 North Bellhaven Rd, Palm Glen, FL 33418</span>
  </footer>
</section>

<section class="sheet sheet--letter">
  <svg class="masthead" viewBox="0 0 949 210" preserveAspectRatio="none"><use href="#masthead-art"/></svg>
  <div class="practice-mark">RB Spine &amp; Vitality Center</div>
  <div class="physicians">
    <div class="physician-name">Esi Dankwa, M.D.</div>
    <div class="physician-specialty">Hip &amp; Knee Replacement / General Orthopaedic Surgery</div>
    <div class="physician-name">Lucinda Pryce, M.D.</div>
    <div class="physician-specialty">Hand and Upper Extremity Surgery</div>
  </div>
  <article class="letter">
    <div class="recipient-name">Dear. Mrs Nora Fields</div>
    <div class="recipient-role">Chief Director</div>
    <div class="letter-date">Date: 07-August-2025</div>
    <div class="letter-body">
      <p>Lorem ipsum dolor sit amet, consectetur adipiscing elit, sed do eiusmod tempor incididunt ut labore et dolore magna aliqua. Sollicitudin ac orci phasellus egestas tellus rutrum tellus. Euismod elementum nisi quis eleifend quam adipiscing vitae proin sagittis. Egestas sed tempus urna et pharetra pharetra. Quis blandit turpis cursus in hac habitasse. Sed velit dignissim sodales ut eu. Ac auctor augue mauris augue neque. In arcu cursus euismod quis viverra nibh cras pulvinar mattis. Libero justo laoreet sit amet. Felis eget nunc lobortis mattis aliquam faucibus purus in. Pulvinar etiam non quam lacus suspendisse faucibus. Odio tempor orci dapibus ultrices. Velit dignissim sodales ut eu sem integer vitae justo. Fermentum et sollicitudin ac orci phasellus egestas. Pharetra vel turpis nunc eget lorem dolor sed. Sed turpis tincidunt id aliquet risus feugiat in ante. Mus mauris vitae ultricies leo integer malesuada nunc vel. Rhoncus urna neque viverra justo nec ultrices dui. Ut placerat orci nulla pellentesque dignissim enim sit amet.</p>
      <p>Bibendum arcu vitae elementum curabitur vitae nunc. Nunc pulvinar sapien et ligula ullamcorper malesuada. At elementum eu facilisis sed. Erat pellentesque adipiscing commodo elit at imperdiet dui accumsan sit. Nunc scelerisque viverra mauris in aliquam sem fringilla. In vitae turpis massa sed. Volutpat ac tincidunt vitae semper quis lectus nulla at. Massa placerat duis ultricies lacus sed turpis. Dui vivamus arcu felis bibendum ut tristique et egestas. Blandit aliquam etiam erat velit scelerisque in dictum non consectetur. Id neque aliquam vestibulum morbi blandit cursus risus at. Sed egestas egestas fringilla phasellus faucibus scelerisque eleifend donec. Ornare quam viverra orci sagittis eu volutpat odio facilisis. Volutpat sed cras ornare arcu dui vivamus arcu. Interdum consectetur libero id faucibus nisl.</p>
      <p>Viverra mauris in aliquam sem. Mattis molestie a iaculis at erat pellentesque adipiscing commodo elit. Sit amet volutpat consequat mauris nunc. Aliquam nulla facilisi cras fermentum. Sed turpis tincidunt id aliquet risus feugiat. Augue neque gravida in fermentum et sollicitudin ac orci.</p>
    </div>
    <div class="signature" role="img" aria-label="Handwritten signature of the sender"></div>
    <div class="signer-name">Daniel Reed Fields</div>
    <div class="signer-role">Chief Director</div>
  </article>
  <footer class="contact-bar">
    <span class="contact-item"><svg><use href="#icon-phone"/></svg>954-218-4635</span>
    <span class="contact-item"><svg><use href="#icon-fax"/></svg>954-581-2264</span>
    <span class="contact-item"><svg><use href="#icon-mail"/></svg>info@myrbspine.example</span>
    <span class="contact-item"><svg><use href="#icon-pin"/></svg>18735 North Bellhaven Rd, Palm Glen, FL 33418</span>
  </footer>
</section>

</body>
</html>
```